Social Media designs (LinkedIn banner, LinkedIn posts, Instagram)

Hello designers!
We are looking to create some more concepts for our social media identity for a search firm (recruitment company)
I have attached a "brand toolkit" that shows our brand, logo, colour scheme to guide you with regards to colours and identiy.

You will see in the brand toolkit there are some examples of;
- A LinkedIn banner for the company (page 23)
- Social Media posts for LinkedIn and Instagram (page 21)

What we are looking for...

We don't really like the current LinkedIn banner ideas. We would like to see more concepts that look more aesthetically pleasing - the current ideas look quite dull.

We DO like the social media post concepts but we would like to have more templates/options that we can use (similar themes)

We welcome submissions for Social Media designs that we can use with our company branding. Thank you for your work in advance!

```html
<!DOCTYPE html>
<html lang="en">
<head>
<meta charset="utf-8">
<title>Case Manager – Social Posts</title>
<link rel="stylesheet" href="https://fonts.googleapis.com/css2?family=Manrope:wght@400;700&display=swap">
<style>
  :root {
    --page-bg: #ffffff;
    --card-bg: #17302a;
    --photo-deep: #142a24;
    --photo-mid: #2c5448;
    --photo-light: #5a8a7d;
    --photo-sky: #6f9992;
    --title-cream: #e8e5dc;
    --accent-green: #4f9a7d;
  }
  * { box-sizing: border-box; margin: 0; padding: 0; }
  html, body {
    width: 1200px; height: 625px; overflow: hidden;
    background: var(--page-bg);
    font-family: "Manrope", sans-serif;
  }
  .post-row { position: relative; width: 1200px; height: 625px; }
  .post {
    position: absolute; top: 122.5px;
    width: 380px; height: 380px;
    background: var(--card-bg);
    overflow: hidden;
  }
  .post--london { left: 17.5px; }
  .post--newyork { left: 410px; }
  .post--barcelona { left: 802.5px; }

  .post__photo {
    position: absolute; left: 69px; top: 0;
    width: 311px; height: 319px;
  }
  .post--london .post__photo {
    background:
      radial-gradient(ellipse 90px 140px at 250px 70px, var(--photo-sky), transparent 70%),
      radial-gradient(ellipse 120px 90px at 170px 260px, var(--photo-light), transparent 75%),
      linear-gradient(115deg, var(--photo-deep) 0%, var(--photo-mid) 45%, var(--photo-deep) 70%, var(--photo-mid) 100%);
  }
  .post--newyork .post__photo {
    background:
      radial-gradient(ellipse 110px 150px at 40px 60px, var(--photo-light), transparent 70%),
      radial-gradient(ellipse 90px 110px at 140px 270px, var(--photo-mid), transparent 75%),
      linear-gradient(200deg, #1d332d 0%, var(--photo-mid) 40%, var(--photo-deep) 75%, #22403a 100%);
  }
  .post--barcelona .post__photo {
    background:
      radial-gradient(ellipse 160px 90px at 230px 60px, var(--photo-sky), transparent 75%),
      radial-gradient(ellipse 140px 60px at 200px 180px, var(--photo-light), transparent 70%),
      linear-gradient(180deg, var(--photo-mid) 0%, #2a4a42 45%, var(--photo-deep) 100%);
  }

  .post__role, .post__specialism {
    position: absolute; left: 17.5px;
    color: var(--title-cream);
    white-space: nowrap;
  }
  .post__role { font-weight: 700; font-size: 46px; line-height: 56px; top: 20px; letter-spacing: 0.3px; }
  .post__specialism { font-weight: 400; font-size: 31px; line-height: 38px; top: 139px; }

  .post__footer {
    position: absolute; left: 17.5px; right: 14px; top: 330px; height: 34px;
    display: flex; align-items: center; justify-content: space-between;
  }
  .brand {
    display: flex; align-items: center; gap: 9px;
    color: var(--title-cream);
    font-size: 14px; line-height: 14px; font-weight: 400;
  }
  .brand__mark { width: 18px; height: 18px; background: var(--accent-green); }
  .post__location { color: var(--accent-green); font-size: 25px; font-weight: 400; }
</style>
</head>
<body>
<main class="post-row">
  <article class="post post--london">
    <div class="post__photo" role="img" aria-label="Teal-toned photo of London glass office towers and a rainy walkway"></div>
    <h2 class="post__role">Case<br>Manager</h2>
    <p class="post__specialism">Enhanced Due<br>Diligance</p>
    <footer class="post__footer">
      <div class="brand"><span class="brand__mark"></span><span>Marlow<br>Reed</span></div>
      <span class="post__location">London - UK</span>
    </footer>
  </article>

  <article class="post post--newyork">
    <div class="post__photo" role="img" aria-label="Teal-toned photo of New York bridge steelwork and skyline"></div>
    <h2 class="post__role">Case<br>Manager</h2>
    <p class="post__specialism">Enhanced Due<br>Diligance</p>
    <footer class="post__footer">
      <div class="brand"><span class="brand__mark"></span><span>Marlow<br>Reed</span></div>
      <span class="post__location">New York - NY</span>
    </footer>
  </article>

  <article class="post post--barcelona">
    <div class="post__photo" role="img" aria-label="Teal-toned photo of a Barcelona avenue with twin towers and a hill beyond"></div>
    <h2 class="post__role">Case<br>Manager</h2>
    <p class="post__specialism">Enhanced Due<br>Diligance</p>
    <footer class="post__footer">
      <div class="brand"><span class="brand__mark"></span><span>Marlow<br>Reed</span></div>
      <span class="post__location">Barcelona, Spain</span>
    </footer>
  </article>
</main>
</body>
</html>
```